New truck wrap

We are a high end design build remodeling company. Looking to elevate the look of our vehicles with standing out and having a pure identity. Classy yet bold

It’s for a varn 2022 T 480 extended cab full bed pickup truck. Currently white on color

Website is www.colbyhaste.com to see a little more about us

```html
<!DOCTYPE html>
<html lang="en">
<head>
<meta charset="utf-8">
<title>Colby Haste Design Build – Truck Wrap Side Layout</title>
<link href="https://fonts.googleapis.com/css2?family=Cinzel:wght@400&family=Cormorant+Garamond:wght@700&family=Montserrat:wght@700&display=swap" rel="stylesheet">
<style>
  :root {
    --brand-blue: #1b7bc4;
    --deep-blue: #1466a8;
    --silver: #b9bcc0;
    --silver-light: #d9dbde;
    --wrap-white: #ffffff;
    --panel-edge: #d4d6d9;
    --backdrop: #f4f4f5;
  }
  html, body {
    margin: 0;
    padding: 0;
    overflow: hidden;
    background: var(--backdrop);
  }
  .canvas {
    position: relative;
    width: 1200px;
    height: 1045px;
    overflow: hidden;
    background: var(--backdrop);
  }
  .wrap-layout {
    position: absolute;
    left: 0;
    top: 0;
    width: 1200px;
    height: 1045px;
  }
  .brand-name {
    font-family: "Cinzel", serif;
    font-weight: 400;
    font-size: 33px;
    fill: var(--brand-blue);
    letter-spacing: 0.5px;
  }
  .service-line {
    font-family: "Montserrat", sans-serif;
    font-weight: 700;
    font-size: 12.5px;
    fill: var(--brand-blue);
    letter-spacing: 0.4px;
  }
  .web-address {
    font-family: "Cormorant Garamond", serif;
    font-weight: 700;
    font-size: 29px;
    fill: var(--wrap-white);
  }
  .phone-number {
    font-family: "Cormorant Garamond", serif;
    font-weight: 700;
    font-size: 40px;
    fill: var(--wrap-white);
    letter-spacing: 1px;
  }
</style>
</head>
<body>
<main class="canvas">
  <svg class="wrap-layout" viewBox="0 0 1200 1045" xmlns="http://www.w3.org/2000/svg">
    <rect class="side-panel" x="20" y="400" width="1160" height="200" rx="18" fill="var(--wrap-white)" stroke="var(--panel-edge)" stroke-width="2"/>

    <polygon class="door-band-silver" points="305,560 760,548 745,572 305,574" fill="var(--silver-light)"/>
    <polygon class="door-band" points="305,570 742,560 722,600 305,600" fill="var(--brand-blue)"/>

    <polygon class="accent-stripe" points="770,430 800,430 735,560 705,560" fill="var(--silver)"/>

    <path class="bed-panel" d="M765 400 L1162 400 Q1180 400 1180 418 L1180 582 Q1180 600 1162 600 L745 600 L760 560 L752 520 Z" fill="var(--brand-blue)"/>
    <polygon class="bed-panel-shade" points="800,600 860,470 900,470 840,600" fill="var(--deep-blue)" opacity="0.5"/>

    <rect class="brand-square" x="310" y="506" width="20" height="20" fill="var(--brand-blue)"/>
    <text class="brand-name" x="338" y="527">Colby Haste</text>

    <text class="service-line" x="706" y="532" text-anchor="end">Home Remodeling</text>
    <text class="service-line" x="706" y="548" text-anchor="end">Design-Build Services</text>

    <text class="web-address" x="335" y="591">colbyhaste.com</text>
    <text class="phone-number" x="875" y="452">215-555-0148</text>
  </svg>
</main>
</body>
</html>
```